Meridian Callware business card design

I would like to see some designs for a business card for Meridian Callware. I would like the business card to be double sided. It will need to have a similar colour / look and feel to our website www.meridiancallware.com.au I have also attached our latest flyer. Final designs to be handed over in Photoshop format so that I can edit the business card when needed please.

Industry/Entity Type

Business

Contact Information for Business Card

Kelvin Ashworth
sales@meridiancallware.com.au
Business Development Manager
ph: (08) 6517 2984
www.meridiancallware.com.au

Font styles to use
Serif
Sans Serif

Requirements
Must have
• If you could please utilise our colour scheme as seen on our website and the attached flyer.
• I would also like the final design to be in a Photoshop format so that I can edit it when needed please.

```html
<!DOCTYPE html>
<html lang="en">
<head>
<meta charset="utf-8">
<title>Meridian Callware – Business Card</title>
<link rel="stylesheet" href="https://fonts.googleapis.com/css2?family=Open+Sans:wght@400;600;700&display=swap">
<style>
  :root {
    --backdrop: #e9e7e3;
    --card-light: #fbfbfb;
    --card-light-edge: #e6e6e6;
    --card-dark: #3b3a3c;
    --card-dark-deep: #2c2b2d;
    --ink: #3a3a3a;
    --ink-soft: #555555;
    --brand-blue: #1a9bc9;
    --white: #ffffff;
  }
  * { box-sizing: border-box; margin: 0; padding: 0; }
  html, body {
    width: 1200px; height: 780px; overflow: hidden;
    background: var(--backdrop);
    font-family: "Open Sans", Arial, sans-serif;
  }
  .sheet {
    width: 1200px; height: 780px;
    display: flex; align-items: center; justify-content: center; gap: 40px;
  }
  .card {
    position: relative;
    width: 540px; height: 330px;
    border-radius: 18px;
    box-shadow: 0 6px 18px rgba(0,0,0,0.18);
    overflow: hidden;
  }
  /* Front */
  .card--front {
    background: linear-gradient(160deg, var(--card-light) 40%, var(--card-light-edge));
  }
  .wordmark {
    display: flex; align-items: center; gap: 12px;
    font-weight: 600; letter-spacing: -0.5px;
  }
  .wordmark__dot {
    width: 14px; height: 14px; border-radius: 50%;
    background: var(--brand-blue);
  }
  .card--front .wordmark {
    position: absolute; left: 40px; top: 42px;
    font-size: 42px; color: var(--ink);
  }
  .identity {
    position: absolute; right: 40px; top: 118px;
    text-align: right;
  }
  .identity__name {
    font-size: 22px; font-weight: 700; color: var(--brand-blue);
    line-height: 1.1;
  }
  .identity__title {
    font-size: 13px; color: var(--ink-soft); margin-top: 2px;
  }
  .divider {
    position: absolute; left: 40px; top: 176px;
    width: 280px; height: 1px; background: var(--ink);
  }
  .contact {
    position: absolute; left: 40px; bottom: 40px;
    list-style: none;
  }
  .contact__item {
    display: flex; align-items: center; gap: 8px;
    font-size: 13.5px; color: var(--ink); line-height: 22px;
  }
  .contact__icon {
    width: 17px; height: 17px; border-radius: 4px;
    background: var(--brand-blue);
    display: flex; align-items: center; justify-content: center;
  }
  .address {
    position: absolute; right: 40px; bottom: 40px;
    text-align: right; font-style: normal;
    font-size: 13.5px; line-height: 22px; color: var(--ink);
  }
  /* Back */
  .card--back {
    background: radial-gradient(ellipse at 40% 30%, var(--card-dark) 30%, var(--card-dark-deep));
    display: flex; align-items: center; justify-content: center;
  }
  .card--back .wordmark {
    font-size: 44px; color: var(--white);
  }
</style>
</head>
<body>
<main class="sheet">
  <section class="card card--front" aria-label="Business card front">
    <div class="wordmark"><span class="wordmark__text">Meridian Callware</span><span class="wordmark__dot"></span></div>

    <div class="identity">
      <p class="identity__name">Kelvin Ashworth</p>
      <p class="identity__title">Business Development Manager</p>
    </div>

    <div class="divider"></div>

    <ul class="contact">
      <li class="contact__item">
        <span class="contact__icon">
          <svg width="11" height="11" viewBox="0 0 24 24"><path fill="#fff" d="M6.6 10.8a15.1 15.1 0 0 0 6.6 6.6l2.2-2.2c.3-.3.7-.4 1-.2 1.1.4 2.3.6 3.6.6.6 0 1 .4 1 1V20c0 .6-.4 1-1 1A17 17 0 0 1 3 4c0-.6.4-1 1-1h3.5c.6 0 1 .4 1 1 0 1.3.2 2.5.6 3.6.1.3 0 .7-.2 1z"/></svg>
        </span>
        (08) 6517 2984
      </li>
      <li class="contact__item">
        <span class="contact__icon">
          <svg width="11" height="11" viewBox="0 0 24 24"><rect x="2" y="5" width="20" height="14" rx="1.5" fill="#fff"/><path d="M3 6l9 7 9-7" fill="none" stroke="#1a9bc9" stroke-width="2"/></svg>
        </span>
        sales@meridiancallware.com.au
      </li>
      <li class="contact__item">
        <span class="contact__icon">
          <svg width="11" height="11" viewBox="0 0 24 24" fill="none" stroke="#fff" stroke-width="2"><circle cx="12" cy="12" r="9"/><path d="M3 12h18M12 3c3 3.5 3 14.5 0 18M12 3c-3 3.5-3 14.5 0 18"/></svg>
        </span>
        www.meridiancallware.com.au
      </li>
    </ul>

    <address class="address">
      Fourth Street<br>
      Ashdale<br>
      Western Australia 6058
    </address>
  </section>

  <section class="card card--back" aria-label="Business card back">
    <div class="wordmark"><span class="wordmark__text">Meridian Callware</span><span class="wordmark__dot"></span></div>
  </section>
</main>
</body>
</html>
```